Modern, upmarket label design for food product

We need a label design for a food company producing nuts with sesame and honey. In fact, we would like the words "Cashews med sesam & honning" on the label (It's in Danish and means - Cashews with sesame & honey). It should be easy for the customer to quickly understand what it is.

It is a shelf product in the competitive food industry, which is why the design should wake the feeling of 'just wanting to grab the product down from the shelves'. So, the design should stand out and have an image of a cool, modern, hip product. This being said, I love a raw & handmade look.

The company is called Pølle. Its origins are from the danish word Tiks that is a Danish slang for yummy. I have uploaded a photo of the package the products will be sold in.

Info & dimensions on bag in picture 1.
Dimensions: 6" x 9" | 15.2 cm x 22.3 cm
Capacity: 8 ounces | 250 grams (based on whole bean coffee)

Picture 2 is the same product, but has the possibility of attaching to a hanger on shelfs.

Picture 3 - I have also uploaded a photo of a product bag, where the hole is linear instead of a round hole. The designer chooses, which bag they will like to work with!

Please let me know if there are any questions!

Target Market(s)

Target market could really be any age, but the design needs to compel the target audience to pick it from the shelves. The package should signal a product you want to hold and have other people seeing you have it. The target audience is people who cares for what they buy, and typically doesn't want a low-end or budget product. They want the whole thing, meaning it has to taste good, look good etc. They are also the type of people who like to show off whatever products they buy by placing them in their houses for their guests to see. Or by uploading pictures of it on social medias.

Industry/Entity Type

It Company

Font styles to use
Other font styles liked:
• Not a must, but I like the 'Panton' script

Requirements
Must have
• My project must have the words 'Cashews med sesam & honning' on the label, so the customer will know within a second what they are looking at and buying.
Nice to have
• I am picturing the label with the words 'Cashews med sesam & honning' as a statement, again, emphasizing how the customer instantly should know what the product is. This being said, it should not be the only thing on the package and I love a raw & handmade look - which inspiration picture 5 is a great example of!
• I have uploaded photos of what I think looks good. With this said, I am not looking for a copy of those products, but see them as good inspiration. I have named the photos inspiration 1, 2, 3, 4 & 5.
• If needed, more text can be put on the label. For example 'vegan', 'laktosefri', Glutenfri', or 'Sund Snack' are great words for being used on the label.
Should not have
• The fonts on the label should not be too decorative. Personally I like an easy too read font.

```html
<!DOCTYPE html>
<html lang="da">
<head>
<meta charset="utf-8">
<title>Pølle – Cashews med sesam &amp; honning</title>
<link rel="stylesheet" href="https://fonts.googleapis.com/css2?family=Cherry+Swash:wght@400;700&family=Josefin+Slab:wght@300;400&display=swap">
<style>
  :root {
    --paper: #ffffff;
    --cocoa: #4a2a1e;
    --honey: #e39a16;
    --stone: #7d706b;
    --honey-soft: rgba(227, 154, 22, 0.18);
  }
  html, body {
    margin: 0;
    padding: 0;
    width: 1200px;
    height: 695px;
    overflow: hidden;
    background: var(--paper);
  }
  .label {
    display: block;
    width: 1200px;
    height: 695px;
  }
  .brand-name {
    font-family: "Cherry Swash", serif;
    font-weight: 700;
    font-size: 46px;
    fill: var(--cocoa);
  }
  .ornament { fill: var(--honey-soft); }
  .crown-arc {
    fill: none;
    stroke: var(--cocoa);
    stroke-width: 3;
    stroke-linecap: round;
  }
  .tagline {
    font-family: "Josefin Slab", serif;
    font-weight: 300;
    font-size: 52px;
    fill: var(--stone);
    letter-spacing: 1px;
  }
  .product-name {
    font-family: "Cherry Swash", serif;
    font-weight: 700;
    font-size: 150px;
    fill: var(--cocoa);
  }
  .ribbon { fill: var(--honey); }
  .ribbon-dot { fill: var(--cocoa); }
  .flavour {
    font-family: "Cherry Swash", serif;
    font-weight: 400;
    font-size: 44px;
    fill: var(--cocoa);
  }
  .net-weight {
    font-family: "Josefin Slab", serif;
    font-weight: 300;
    font-size: 32px;
    fill: var(--stone);
  }
</style>
</head>
<body>
<svg class="label" viewBox="0 0 1200 695" xmlns="http://www.w3.org/2000/svg">
  <defs>
    <path id="tagline-curve" d="M420,292 Q600,180 780,292"/>
    <path id="flavour-curve" d="M330,500 Q600,438 870,500"/>
  </defs>

  <rect class="ornament" x="380" y="92" width="140" height="158" rx="40" role="img" aria-label="Hand-drawn honey-coloured swirl flourish"/>
  <rect class="ornament" x="680" y="92" width="140" height="158" rx="40" role="img" aria-label="Hand-drawn honey-coloured swirl flourish"/>

  <text class="brand-name" x="600" y="162" text-anchor="middle">Pølle</text>

  <path class="crown-arc" d="M325,300 Q600,70 875,300"/>

  <text class="tagline" text-anchor="middle">
    <textPath href="#tagline-curve" startOffset="50%">Sund Snack</textPath>
  </text>

  <text class="product-name" x="600" y="405" text-anchor="middle" textLength="560" lengthAdjust="spacingAndGlyphs">cashews</text>

  <path class="ribbon" d="M275,447 Q600,380 930,447 L942,522 Q600,452 283,522 Z"/>
  <circle class="ribbon-dot" cx="312" cy="490" r="4"/>
  <circle class="ribbon-dot" cx="905" cy="490" r="4"/>
  <text class="flavour" text-anchor="middle">
    <textPath href="#flavour-curve" startOffset="50%">med sesam &amp; honning</textPath>
  </text>

  <text class="net-weight" x="600" y="615" text-anchor="middle">8 oz</text>
</svg>
</body>
</html>
```